QV Pathway Branding
Stationary - Business Card, Letter Head, Powerpoint file, Word Document, Email Signature.
QV Pathway Branding - Information Technology
Creative Brief
Professional
Darren M. L.
Founder
58 Ravel Pine Street #04-12 Orlan Plaza Singapore 142390
darrenm.l@qvpathway-example.com
www.qvpathway-example.com
BRN : 209874163K
The main idea of this contest is not just for the name card but a branding for our stationary. The following are the pointers/comments. I would like it if Icons were used Instead of Phone, Fax, Email, Web. Note: the 2 different Phone numbers in the Cell phone, each should have it's own line if possible. Please use white matte background. For additional effects on the namecard, you may use the different shades to create the effect. For Stationary, please ensure a word document format, powerpoint and email signature format is created as well as the other conventional document types. BRN is only required on the Letterheads. Extra type of formats for branding (e.g. Folder design) earns you extra Stars and ultimately seals the deal with creativity.
Please be creative in the design of the back of the business card. You are to freely manipulate the details given for back and front. Which means you may incorporate in the details in the design to be either the front and or the back.

```html
<!DOCTYPE html>
<html lang="en">
<head>
<meta charset="utf-8">
<title>QV Pathway Branding – Stationery Set</title>
<link href="https://fonts.googleapis.com/css2?family=Roboto+Condensed:wght@700&family=Open+Sans:wght@400;600;700&display=swap" rel="stylesheet">
<style>
:root{
  --red:#e2231a;
  --red-dark:#b5170f;
  --ink:#222;
  --grey:#8a8a8a;
  --rule:#d9d9d9;
  --paper:#ffffff;
  --black:#111;
  --stage:#e9e6e2;
}
*{box-sizing:border-box;margin:0;padding:0}
html,body{width:1200px;height:686px;overflow:hidden}
body{background:var(--stage);font-family:"Open Sans",Arial,sans-serif;color:var(--ink);position:relative}
.piece{position:absolute;background:var(--paper);overflow:hidden;box-shadow:0 2px 5px rgba(0,0,0,.25)}
.logo{font-family:"Roboto Condensed","Arial Narrow",sans-serif;font-weight:700;color:var(--ink);letter-spacing:-.2px;display:flex;align-items:center;gap:3px;white-space:nowrap;line-height:1}
.logo .dot{display:inline-block;border-radius:50%;background:var(--red)}
.logo.on-dark{color:#fff}
.logo.sm{font-size:11px}.logo.sm .dot{width:6px;height:6px}
.logo.md{font-size:15px}.logo.md .dot{width:8px;height:8px}
.logo.lg{font-size:20px}.logo.lg .dot{width:10px;height:10px}
.tiny{font-size:4px;line-height:1.45;color:#444;white-space:nowrap}
.name{color:var(--red);font-weight:700;font-size:5.5px}
.role{font-size:4px;color:#555}
.foot{position:absolute;left:0;right:0;bottom:0;background:var(--red);color:#fff;font-size:4px;display:flex;align-items:center;justify-content:flex-end;padding-right:6px;white-space:nowrap}
.lines i{display:block;height:2px;background:#e6e6e6;margin-bottom:4px}
.contact-row{display:flex;align-items:center;gap:2px}
.contact-row svg{width:4px;height:4px;flex:none}
.table{border:1px solid #999;position:absolute}
.table .row{height:5px;border-bottom:1px solid #ccc}
.slide-title{font-weight:700;color:var(--red);font-size:9px;white-space:nowrap}
.slide-head{font-weight:700;font-size:8px;color:#fff;display:flex;align-items:center;gap:4px}
.folder-cover{background:var(--red)}
</style>
</head>
<body>

<!-- Business card front with contacts -->
<div class="piece" style="left:36px;top:36px;width:149px;height:84px">
  <div class="logo sm" style="position:absolute;left:8px;top:10px">QV PATHWAY<span class="dot"></span></div>
  <div style="position:absolute;left:8px;top:34px"><div class="name">Darren M. L.</div><div class="role">Founder</div></div>
  <div class="tiny" style="position:absolute;left:80px;top:30px">
    <div class="contact-row"><svg viewBox="0 0 4 4"><rect width="4" height="4" fill="#e2231a"/></svg>+65 6123 4567</div>
    <div class="contact-row"><svg viewBox="0 0 4 4"><rect width="4" height="4" fill="#e2231a"/></svg>+65 9123 4567</div>
    <div class="contact-row"><svg viewBox="0 0 4 4"><rect width="4" height="4" fill="#e2231a"/></svg>+65 6123 4568</div>
    <div class="contact-row"><svg viewBox="0 0 4 4"><rect width="4" height="4" fill="#e2231a"/></svg>darrenml</div>
  </div>
  <div class="foot" style="height:7px">www.qvpathway-example.com</div>
</div>

<!-- Business card with red band -->
<div class="piece" style="left:36px;top:125px;width:149px;height:84px">
  <div class="logo sm" style="position:absolute;left:8px;top:10px">QV PATHWAY<span class="dot"></span></div>
  <div style="position:absolute;left:0;top:36px;width:70px;height:14px;background:var(--red);padding:2px 8px">
    <div style="color:#fff;font-weight:700;font-size:5.5px">Darren M. L.</div><div style="color:#fff;font-size:3.5px">Founder</div>
  </div>
  <div class="tiny" style="position:absolute;left:80px;top:32px">
    <div>+65 6123 4567</div><div>+65 9123 4567</div><div>+65 6123 4568</div><div>darrenml</div>
  </div>
  <div class="foot" style="height:7px">www.qvpathway-example.com</div>
</div>

<!-- Business card backs, white -->
<div class="piece" style="left:197px;top:36px;width:149px;height:84px">
  <div class="tiny" style="position:absolute;left:80px;top:14px">
    <div>+65 6123 4567</div><div>+65 9123 4567</div><div>+65 6123 4568</div><div>darrenml</div>
  </div>
  <div class="logo sm" style="position:absolute;left:8px;top:40px">QV PATHWAY<span class="dot"></span></div>
  <div class="foot" style="height:7px">www.qvpathway-example.com</div>
</div>
<div class="piece" style="left:197px;top:125px;width:149px;height:84px">
  <div class="logo md" style="position:absolute;left:30px;top:36px">QV PATHWAY<span class="dot"></span></div>
  <div class="foot" style="height:7px">www.qvpathway-example.com</div>
</div>

<!-- Business card backs, black -->
<div class="piece" style="left:355px;top:36px;width:149px;height:84px;background:var(--black)">
  <div class="logo md on-dark" style="position:absolute;left:30px;top:36px">QV PATHWAY<span class="dot"></span></div>
</div>
<div class="piece" style="left:355px;top:125px;width:149px;height:84px;background:var(--black)">
  <div class="logo md on-dark" style="position:absolute;left:30px;top:36px">QV PATHWAY<span class="dot"></span></div>
</div>

<!-- Letterhead -->
<div class="piece" style="left:516px;top:36px;width:192px;height:269px">
  <div class="logo md" style="position:absolute;left:12px;top:14px">QV PATHWAY<span class="dot"></span></div>
  <div class="tiny" style="position:absolute;right:12px;top:12px;text-align:right">
    <div>58 Ravel Pine Street #04-12</div><div>Orlan Plaza Singapore 142390</div><div>+65 6123 4567</div><div>darrenm.l@qvpathway-example.com</div><div>BRN : 209874163K</div>
  </div>
  <div class="lines" style="position:absolute;left:12px;right:12px;top:70px"><i></i><i></i><i></i><i style="width:70%"></i></div>
  <div class="foot" style="height:10px">www.qvpathway-example.com</div>
</div>

<!-- Invoice -->
<div class="piece" style="left:725px;top:36px;width:192px;height:269px">
  <div class="logo md" style="position:absolute;left:12px;top:14px">QV PATHWAY<span class="dot"></span></div>
  <div class="tiny" style="position:absolute;right:12px;top:12px;text-align:right">
    <div>INVOICE</div><div>No. 0001</div><div>Date: 01/01</div><div>BRN : 209874163K</div>
  </div>
  <div class="table" style="left:12px;right:12px;top:62px;height:130px">
    <div class="row" style="background:#bbb"></div><div class="row"></div><div class="row"></div><div class="row"></div><div class="row"></div><div class="row"></div><div class="row"></div><div class="row"></div><div class="row"></div><div class="row"></div>
  </div>
  <div class="tiny" style="position:absolute;left:12px;top:200px">Please make payment to QV Pathway</div>
  <div class="foot" style="height:10px">www.qvpathway-example.com</div>
</div>

<!-- Fax / memo -->
<div class="piece" style="left:936px;top:36px;width:192px;height:269px">
  <div class="logo md" style="position:absolute;left:12px;top:14px">QV PATHWAY<span class="dot"></span></div>
  <div class="tiny" style="position:absolute;right:12px;top:12px;text-align:right">
    <div>FAX</div><div>To:</div><div>From:</div><div>Pages:</div>
  </div>
  <div class="tiny" style="position:absolute;left:12px;top:56px;display:flex;gap:14px">
    <span>□ Urgent</span><span>□ Review</span><span>□ Reply</span><span>□ Note</span>
  </div>
  <div class="lines" style="position:absolute;left:12px;right:12px;top:72px"><i></i><i></i></div>
  <div class="foot" style="height:10px">www.qvpathway-example.com</div>
</div>

<!-- Presentation slides -->
<div class="piece" style="left:36px;top:319px;width:199px;height:146px">
  <div class="logo lg" style="position:absolute;left:14px;top:20px">QV PATHWAY<span class="dot"></span></div>
  <div style="position:absolute;left:14px;top:66px"><div class="slide-title">YOUR TITLE GOES HERE</div><div style="font-size:6px;color:#555">Subtitle Name</div></div>
  <div class="foot" style="height:9px">www.qvpathway-example.com</div>
</div>
<div class="piece" style="left:247px;top:319px;width:199px;height:146px">
  <div style="height:20px;background:var(--black);padding-left:10px" class="slide-head"><span class="logo sm on-dark"><span class="dot"></span></span>ABOUT US</div>
  <div class="foot" style="height:9px">www.qvpathway-example.com</div>
</div>
<div class="piece" style="left:36px;top:474px;width:199px;height:92px">
  <div class="logo md" style="position:absolute;left:14px;top:12px">QV PATHWAY<span class="dot"></span></div>
  <div style="position:absolute;left:14px;top:46px"><div class="slide-title" style="font-size:7px">THANK YOU FOR YOUR ATTENTION</div><div style="font-size:5px;color:#555">PRESENTER</div></div>
  <div class="foot" style="height:8px">www.qvpathway-example.com</div>
</div>
<div class="piece" style="left:247px;top:474px;width:199px;height:92px">
  <div style="padding:8px 10px" class="slide-head"><span class="logo sm"><span class="dot"></span></span><span style="color:var(--ink)">ABOUT US</span></div>
  <div class="foot" style="height:8px">www.qvpathway-example.com</div>
</div>

<!-- Email signature -->
<div class="piece" style="left:36px;top:578px;width:410px;height:70px">
  <div class="logo md" style="position:absolute;left:12px;top:12px">QV PATHWAY<span class="dot"></span></div>
  <div style="position:absolute;left:120px;top:10px"><div class="name">Darren M. L.</div><div class="role">Founder</div></div>
  <div class="tiny" style="position:absolute;left:200px;top:10px">
    <div>+65 6123 4567</div><div>+65 9123 4567</div><div>darrenm.l@qvpathway-example.com</div>
  </div>
  <div class="foot" style="height:8px">www.qvpathway-example.com</div>
</div>

<!-- DL envelope -->
<div class="piece" style="left:492px;top:396px;width:209px;height:96px">
  <div class="logo sm" style="position:absolute;left:10px;top:10px">QV PATHWAY<span class="dot"></span></div>
  <div class="tiny" style="position:absolute;left:10px;top:24px">58 Ravel Pine Street #04-12<br>Orlan Plaza Singapore 142390</div>
  <div class="foot" style="height:7px">www.qvpathway-example.com</div>
</div>

<!-- Envelope back with red flap -->
<div class="piece" style="left:936px;top:319px;width:192px;height:132px">
  <svg width="192" height="132" viewBox="0 0 192 132" style="position:absolute;inset:0">
    <polygon points="0,0 192,0 192,30 96,66 0,30" fill="#e2231a"/>
    <line x1="0" y1="132" x2="96" y2="80" stroke="#ddd"/>
    <line x1="192" y1="132" x2="96" y2="80" stroke="#ddd"/>
  </svg>
</div>

<!-- Folder inside -->
<div class="piece" style="left:492px;top:504px;width:324px;height:156px">
  <div style="position:absolute;left:161px;top:0;bottom:0;width:1px;background:var(--rule)"></div>
  <svg width="324" height="60" viewBox="0 0 324 60" style="position:absolute;left:0;bottom:0">
    <path d="M0 14 H150 L160 60 H0Z" fill="#e2231a"/>
    <path d="M324 14 H174 L164 60 H324Z" fill="#e2231a"/>
  </svg>
  <div class="piece" style="left:42px;top:112px;width:60px;height:30px">
    <div class="logo" style="font-size:6px;position:absolute;left:4px;top:5px">QV PATHWAY<span class="dot" style="width:3px;height:3px"></span></div>
    <div class="foot" style="height:4px"></div>
  </div>
</div>

<!-- Folder cover -->
<div class="piece folder-cover" style="left:828px;top:504px;width:300px;height:156px">
  <div style="position:absolute;left:150px;top:0;bottom:0;width:1px;background:var(--red-dark)"></div>
  <div class="logo md on-dark" style="position:absolute;left:186px;top:66px">QV PATHWAY<span class="dot" style="background:#fff"></span></div>
  <div style="position:absolute;left:12px;top:110px;color:#fff;font-size:4px;line-height:1.5">58 Ravel Pine Street #04-12<br>Orlan Plaza Singapore 142390<br>www.qvpathway-example.com</div>
</div>

</body>
</html>
```